TARPLOAD business card design

TARPLOAD is a manufacturer of skip bags supplying both the domestic and commercial market. We wish to convey core characteristics of strength, professionalism and reliability to our customers. We are after a business card that uses our company colours of black and yellow as well as incorporating our logo. Our customers are predominantly in the construction or hardware industry. It is important the cards are professional as we are a small company wishing to appear larger than we actually are. more info on the company and product available at www.tarpload-example.com.au

Target Market(s)

hardware buyers, contruction company owners

Industry/Entity Type

Construction

Requirements
Must have
• company colours of black and yellow - No other colours or variation of yellow black. our company logo. card design must convey "tough"
• Card design must be landscape
• Details to be included on the card are:
• Name and Tiltle
• Phone number : 1300 41 62 53
• Mobile: 0452 718 903
• Fax: 03 9617 4852
• email: dale.hendry@tarpload-example.com.au
• address: PO Box 517, Kelvindale, VIC,3294
• Text in white when on a black background
Nice to have
• I like the idea of the back of the card being black with lighter circle area in the middle with black logo in the centre. Similar to the attached "iconic" card

```html
<!DOCTYPE html>
<html lang="en">
<head>
<meta charset="utf-8">
<title>TARPLOAD business card</title>
<link rel="stylesheet" href="https://fonts.googleapis.com/css2?family=Arimo:ital,wght@0,400;0,700;1,700&family=Oswald:wght@700&display=swap">
<style>
  :root {
    --page: #ffffff;
    --yellow: #f2cd00;
    --black: #000000;
    --rule: #555555;
    --frame: #9a9a9a;
    --faint: #dcdddf;
    --glow: #d4d4d4;
    --ink: #111111;
  }
  * { margin: 0; padding: 0; box-sizing: border-box; }
  html, body {
    width: 848px; height: 1200px; overflow: hidden;
    background: var(--page);
  }
  body { position: relative; font-family: "Arimo", Arial, sans-serif; color: var(--ink); }

  .card { position: absolute; left: 212px; width: 367px; height: 224px; overflow: hidden; }

  /* Front */
  .card-front { top: 186px; background: var(--page); border: 1px solid var(--frame); }
  .side-band { position: absolute; left: 0; top: 0; width: 68px; height: 100%; background: var(--yellow); }
  .side-rule { position: absolute; left: 70px; top: 0; width: 3px; height: 100%; background: var(--rule); }
  .band-brand {
    position: absolute; left: 0; top: 30px; width: 68px; text-align: center;
    font-family: "Oswald", Impact, sans-serif; font-weight: 700;
    font-size: 12px; letter-spacing: 0.2px; color: var(--black);
  }
  .holder { position: absolute; right: 10px; top: 13px; text-align: right; }
  .holder-name { font-weight: 700; font-style: italic; font-size: 11.5px; color: var(--black); }
  .holder-title { font-weight: 700; font-size: 9.5px; color: var(--yellow); margin-top: 1px; }
  .details { position: absolute; left: 85px; top: 62px; font-size: 9px; line-height: 12px; }
  .details p + p { margin-top: 12px; }
  .details .label { display: inline-block; width: 30px; }
  .details .label-wide { display: inline-block; width: 42px; }
  .corner-block {
    position: absolute; right: 0; bottom: 0; width: 80px; height: 78px;
    background: var(--faint);
  }

  /* Back */
  .card-back {
    top: 493px;
    background: radial-gradient(ellipse 52% 62% at 50% 50%, var(--glow) 0%, #6e6e6e 35%, #2a2a2a 70%, var(--black) 100%);
  }
  .back-brand {
    position: absolute; left: 0; right: 0; top: 128px; text-align: center;
    font-family: "Oswald", Impact, sans-serif; font-weight: 700;
    font-size: 36px; line-height: 1; letter-spacing: 1px; color: var(--black);
  }
</style>
</head>
<body>

<section class="card card-front" aria-label="Card front">
  <div class="side-band"></div>
  <div class="side-rule"></div>
  <div class="band-brand">TARPLOAD</div>

  <div class="holder">
    <div class="holder-name">PERSON NAME</div>
    <div class="holder-title">Designation</div>
  </div>

  <div class="details">
    <p>xx/xx, Level 1,<br>Suburb, State, Pin</p>
    <p><span class="label">L/L</span>: 00 0000 0000<br>
       <span class="label">Mob</span>: 0000 000 000<br>
       <span class="label">Fax</span>: 00 0000 0000</p>
    <p><span class="label-wide">E-mail</span>: abc@xyz.com.au<br>
       <span class="label-wide">Website</span>: www.xyz.com.au</p>
  </div>

  <div class="corner-block" role="img" aria-label="Faint grey brand decoration"></div>
</section>

<section class="card card-back" aria-label="Card back">
  <div class="back-brand">TARPLOAD</div>
</section>

</body>
</html>
```